Home loan flyer design - home builders

My mortgage broker firms requires a DL flyer targeting who need finance to build their home.

The design must be professional in presentation as we a small boutique firm that build relationships with our clients through trust.

Refer to my website marlowfinance.com.au to keep the design in similar taste.

Target Market(s)

People in the market to build their 1st home, investment or upgrade.

Industry/Entity Type

Finance

Colors
ec1f27
ffffff
000000

Requirements
Must have
• Catching to the eye. These flyers will be sitting on the desk at builders display homes with many other brochures.
• Premium feel to the design / branding.
Nice to have
• connect to the emotional feelings of building. Not the transaction. ie building a future for the kids or building their investment portfolio which brings financial freedom etc etc
Should not have
• No money pictures

```html
<!DOCTYPE html>
<html lang="en">
<head>
<meta charset="utf-8">
<title>Marlow Finance – Building a Home DL Flyer</title>
<link href="https://fonts.googleapis.com/css2?family=Carlito:wght@400;700&display=swap" rel="stylesheet">
<style>
  :root {
    --brand-red: #d7222b;
    --ink: #000000;
    --paper: #ffffff;
    --body-grey: #6a6a6a;
    --footer-dark: #3b3b3d;
    --backdrop: #e9e9e9;
    --scale: 0.903;
  }
  * { box-sizing: border-box; margin: 0; padding: 0; }
  html, body {
    width: 911px; height: 1200px; overflow: hidden;
    background: var(--backdrop);
  }
  .canvas { position: relative; width: 911px; height: 1200px; }
  .flyer {
    position: absolute; left: 189px; top: 40px;
    width: 590px; height: 1240px;
    transform: scale(var(--scale)); transform-origin: top left;
    background: var(--paper);
    font-family: "Carlito", "Calibri", sans-serif;
    box-shadow: 0 4px 14px rgba(0,0,0,.18);
  }
  .hero-photo {
    position: absolute; left: 0; top: 0; width: 590px; height: 445px;
    background:
      linear-gradient(180deg, #c9d2d8 0%, #dcd4bf 30%, #d8bb8a 60%, #c8a270 85%, #b89468 100%);
  }
  .headline-plate {
    position: absolute; left: 0; top: 377px; width: 397px; height: 68px;
    background: rgba(255,255,255,.62);
  }
  .headline {
    position: absolute; left: 24px; top: 388px;
    font-size: 40px; font-weight: 700; color: var(--brand-red);
    letter-spacing: -0.3px; line-height: 1;
  }
  .tagline-band {
    position: absolute; left: 0; top: 445px; width: 590px; height: 66px;
    background: var(--brand-red);
  }
  .tagline {
    position: absolute; left: 24px; top: 17px;
    font-size: 33px; font-weight: 700; color: var(--paper);
    letter-spacing: -0.3px; line-height: 1;
  }
  .copy {
    position: absolute; left: 31px; top: 543px; width: 529px;
    font-size: 22.5px; line-height: 30px; text-align: justify;
  }
  .copy p { margin-bottom: 30px; color: var(--body-grey); }
  .copy .lead { color: var(--ink); }
  .copy .highlight { color: var(--brand-red); }
  .brand {
    position: absolute; left: 88px; top: 1010px;
    display: flex; align-items: center; gap: 24px;
  }
  .brand-dot {
    width: 92px; height: 92px; border-radius: 50%;
    background: var(--brand-red);
  }
  .brand-name {
    font-size: 50px; font-weight: 400; color: var(--ink); letter-spacing: -0.5px;
  }
  .footer-rule {
    position: absolute; left: 0; top: 1125px; width: 590px; height: 14px;
    background: var(--brand-red);
  }
  .footer {
    position: absolute; left: 0; top: 1139px; width: 590px; height: 101px;
    background: var(--footer-dark); color: var(--paper);
    text-align: center; font-size: 20px;
  }
  .footer .address { position: absolute; left: 0; right: 0; top: 20px; }
  .footer .web { position: absolute; left: 0; right: 0; top: 60px; font-size: 21px; }
</style>
</head>
<body>
<div class="canvas">
  <article class="flyer">
    <div class="hero-photo" role="img" aria-label="Photo of a smiling family of three standing inside the timber wall frames of their new home under construction"></div>
    <div class="headline-plate"></div>
    <h1 class="headline">BUILDING A HOME?</h1>
    <div class="tagline-band"><h2 class="tagline">GET THE FOUNDATIONS RIGHT.</h2></div>

    <section class="copy">
      <p class="lead">Sometimes the hardest part about building your home is organising the finance. And if you’ve ever done it before, you’ll know it can be trickier than your average mortgage.</p>
      <p>Whether it is your first build, an investment property or even an upgrade—its worth getting in touch.</p>
      <p>I will&nbsp; help you find a great home loan, while talking you through ways to reduce your costs and maximise the value of the build.</p>
      <p><span class="highlight">GET YOUR FINANCIAL FOUNDATIONS RIGHT</span>—it could make all the difference to the affordability of your project.</p>
    </section>

    <div class="brand">
      <span class="brand-dot"></span>
      <span class="brand-name">MarlowFinance</span>
    </div>

    <div class="footer-rule"></div>
    <footer class="footer">
      <div class="address">18 Harbour Street, West Carrington NSW 2324 &nbsp;|&nbsp; 02 4055 7821</div>
      <div class="web">www.marlowfinance.com.au</div>
    </footer>
  </article>
</div>
</body>
</html>
```